Accountants Stationary Package

Letter head, compliment slip, business card, report cover

Using selected logo which will be supplied when available design with compliment slip, letter head, business card and report cover. Some information to be amended and will be supplied at revision stage, design needs to resonate with chosen logo.
Updates

Update information 1 business card - my name is "Martin Keale" post numerals are FCA , TITLE = Managing Director, (but maybe chartered accountant) is ok, my personal mobile is 0417 58 63 14 and personal email ids martin.k@kealeledger.example,au, I like the tag line included " everybody ....succcess" Don't want professional liability logo but ok with the CA and tallo logo I like the colours I like the blue back where it has a soft watermark finish 2. letterheads Need logos for tallo, CA, professional standards Needs full company name and ABN NUMmber as - Keale Ledger Pty Limited, ACN 708 341 256 Linked in ? I am also ok with initials instead of icons for phone, email, fax mobile, etc

Industry/Entity Type

Accounting

Requirements
Must have
• Keale Ledger Pty Limited
• ABN 456456456
• Charted accountants
• Telephone 612 48856302
• Fax 612 4859 0418
• Po Box 6542, Erina, NSW, 2250
• Mobile 0417 586 314
• Address 41 Mulvane road, Erina, suite 9 Mulvane Point
• Mail@kealeledger.example.com.au
• Website kealeledger.example.com.au
• List of services;
• Tax and Accounting
• Business Development
• Superannuation and Financial Services

```html
<!DOCTYPE html>
<html lang="en">
<head>
<meta charset="utf-8">
<title>Keale Ledger — Letterhead</title>
<link rel="stylesheet" href="https://fonts.googleapis.com/css2?family=Open+Sans:wght@400;600;700&display=swap">
<style>
  :root {
    --backdrop: #e6e6e6;
    --paper: #fbfbfb;
    --brand-blue: #1b9ad6;
    --brand-orange: #e8562a;
    --brand-green: #7ab929;
    --ink: #555555;
    --band: #333333;
  }
  * { box-sizing: border-box; margin: 0; padding: 0; }
  html, body {
    width: 1200px;
    height: 795px;
    overflow: hidden;
    background: var(--backdrop);
    font-family: "Open Sans", Arial, sans-serif;
  }
  .letterhead {
    position: absolute;
    left: 330px;
    top: 16px;
    width: 540px;
    height: 763px;
    background: var(--paper);
    box-shadow: 0 2px 10px rgba(0,0,0,0.12);
  }
  .brand {
    position: absolute;
    left: 38px;
    top: 54px;
    display: flex;
    align-items: center;
    gap: 8px;
  }
  .brand-mark {
    width: 20px;
    height: 20px;
    background: var(--brand-blue);
  }
  .brand-name {
    color: var(--brand-blue);
    font-weight: 600;
    font-size: 21px;
    line-height: 24px;
    letter-spacing: 0.5px;
    white-space: nowrap;
  }
  .contact {
    position: absolute;
    top: 46px;
    right: 38px;
    display: flex;
    gap: 16px;
    font-size: 7px;
    line-height: 10px;
    color: var(--ink);
    white-space: nowrap;
  }
  .contact .label { color: var(--brand-blue); font-weight: 700; }
  .contact .abn { color: var(--brand-orange); font-weight: 700; }
  .services {
    position: absolute;
    left: 38px;
    bottom: 22px;
    font-size: 9.5px;
    color: var(--ink);
    white-space: nowrap;
  }
  .services .label { color: var(--brand-blue); font-weight: 600; }
  .services .sep { margin: 0 6px; }
  .base-band {
    position: absolute;
    left: 0;
    right: 0;
    bottom: 0;
    height: 7px;
    background: var(--band);
  }
</style>
</head>
<body>
  <main class="letterhead">
    <header class="brand">
      <span class="brand-mark"></span>
      <span class="brand-name">KEALE LEDGER</span>
    </header>

    <section class="contact">
      <div class="contact-col">
        <p class="abn">ABN 456456456</p>
        <p><span class="label">Address</span> 41 Mulvane road, Corliss Bay,</p>
        <p>suite 9 Mulvane Point</p>
        <p>Po Box 6542, Corliss Bay, NSW, 2299</p>
      </div>
      <div class="contact-col">
        <p><span class="label">Telephone</span> 612 48856302</p>
        <p><span class="label">Fax</span> 612 4859 0418</p>
        <p><span class="label">Mobile</span> 0417 586 314</p>
        <p><span class="label">Email</span> Mail@kealeledger.example.com.au</p>
        <p><span class="label">Website</span> kealeledger.example.com.au</p>
      </div>
    </section>

    <footer class="services">
      <span class="label">List of services :</span>
      Tax and Accounting<span class="sep">|</span>Business Development<span class="sep">|</span>Superannuation<span class="sep">|</span>and Financial Services
    </footer>
    <div class="base-band"></div>
  </main>
</body>
</html>
```